2 Business Card Designs

Need two business cards designed:
1) for lumora studio (wedding video) website is lumorastudio.com.au
2) for lumora studio (corporate video) website is lumorastudio.net.au

I am looking for something simple, no fancy shapes etc. Just elegant, simple and classy.

Both companies are video companies, one specialising in weddings the other corporate videos. Neither card needs to have any pics of video or camera related images. Please use same colour schemes as respective websites.

Logo is the same but can change colour.

Industry/Entity Type

Camera

Requirements
Must have
• Logo should be either all white or a colour to match websites
Should not have
• swirls, flowers, shapes, etc.

```html
<!DOCTYPE html>
<html lang="en">
<head>
<meta charset="utf-8">
<title>Lumora Studio – Business Cards</title>
<link rel="stylesheet" href="https://fonts.googleapis.com/css2?family=Questrial&display=swap">
<style>
  :root {
    --backdrop: #e4e4e2;
    --card-face: #f4f4f3;
    --card-texture: #e9e9e8;
    --ink-dark: #2b2b2b;
    --ink-olive: #6f7363;
    --band-corporate: #262626;
    --band-wedding: #767a68;
    --band-text: #f2f2f0;
  }
  * { box-sizing: border-box; margin: 0; padding: 0; }
  html, body {
    width: 1200px;
    height: 900px;
    overflow: hidden;
    background: var(--backdrop);
    font-family: "Questrial", "Century Gothic", sans-serif;
  }
  .card-sheet {
    width: 1200px;
    height: 900px;
    display: flex;
    flex-direction: column;
    align-items: center;
    justify-content: center;
    gap: 32px;
  }
  .business-card {
    position: relative;
    width: 640px;
    height: 366px;
    border-radius: 18px;
    overflow: hidden;
    background: var(--card-face);
    box-shadow: 0 6px 18px rgba(0, 0, 0, 0.12);
    display: flex;
    flex-direction: column;
  }
  .card-face {
    position: relative;
    flex: 1;
    display: flex;
    align-items: center;
    justify-content: center;
  }
  .name-texture {
    position: absolute;
    inset: 0;
    background: var(--card-texture);
  }
  .brand-name {
    position: relative;
    text-align: center;
    font-weight: 400;
    line-height: 1;
  }
  .brand-name .brand-main {
    display: block;
    font-size: 86px;
    letter-spacing: 1px;
  }
  .brand-name .brand-sub {
    display: block;
    font-size: 26px;
    letter-spacing: 16px;
    margin-top: 6px;
    padding-left: 16px;
    text-transform: uppercase;
  }
  .card--corporate .brand-name { color: var(--ink-dark); }
  .card--wedding .brand-name { color: var(--ink-olive); }
  .service-band {
    height: 80px;
    display: flex;
    align-items: center;
    justify-content: center;
    color: var(--band-text);
    font-size: 22px;
    letter-spacing: 1px;
  }
  .card--corporate .service-band { background: var(--band-corporate); }
  .card--wedding .service-band { background: var(--band-wedding); }
</style>
</head>
<body>
  <main class="card-sheet">
    <article class="business-card card--corporate">
      <div class="card-face">
        <div class="name-texture" role="img" aria-label="Faint repeating wordmark text pattern across the card face"></div>
        <h1 class="brand-name"><span class="brand-main">lumora</span><span class="brand-sub">studio</span></h1>
      </div>
      <div class="service-band">Corporate Video</div>
    </article>

    <article class="business-card card--wedding">
      <div class="card-face">
        <div class="name-texture" role="img" aria-label="Faint repeating wordmark text pattern across the card face"></div>
        <h2 class="brand-name"><span class="brand-main">lumora</span><span class="brand-sub">studio</span></h2>
      </div>
      <div class="service-band">Wedding Video</div>
    </article>
  </main>
</body>
</html>
```